Business Card Design

I would like a simple logo for Harwick Group.
We run a company that looks after our extended
family's investments.

Industry/Entity Type

Business

Contact Information for Business Card

Maureen Blake
Director
Harwick Group
ABN 48 317 602 559
Investment Management
maureen@harwickgroup.com.au
Mobile +61 438 907 615
Level 1, 317 Carrow St
Townsville, Qld 4810

```html
<!DOCTYPE html>
<html lang="en">
<head>
<meta charset="utf-8">
<title>Harwick Group – Business Card</title>
<link rel="stylesheet" href="https://fonts.googleapis.com/css2?family=Open+Sans:wght@600&family=Oswald:wght@500&family=Old+Standard+TT:wght@400;700&display=swap">
<style>
  :root {
    --backdrop: #d9d9d9;
    --card-white: #ffffff;
    --brand-red: #d71920;
    --brand-red-deep: #a80f14;
    --ink: #111111;
    --panel-black: #0d0d0d;
    --panel-charcoal: #262626;
    --text-light: #f2f2f2;
  }
  * { box-sizing: border-box; margin: 0; padding: 0; }
  html, body {
    width: 1200px; height: 900px; overflow: hidden;
    background: var(--backdrop);
  }
  .canvas {
    position: relative; width: 1200px; height: 900px;
  }
  .business-card {
    position: absolute; left: 140px; top: 180px;
    width: 920px; height: 540px;
    border-radius: 34px; overflow: hidden;
    background: var(--card-white);
    box-shadow: 0 18px 40px rgba(0,0,0,0.22);
  }
  .brand-area {
    position: absolute; left: 0; top: 0; width: 100%; height: 250px;
    background: var(--card-white);
  }
  .brand-mark {
    position: absolute; left: 52px; top: 42px;
    width: 170px; height: 170px; border-radius: 50%;
    background: var(--brand-red);
  }
  .brand-name {
    position: absolute; left: 262px; top: 58px;
    font-family: "Open Sans", sans-serif; font-weight: 600;
    font-size: 70px; line-height: 1; color: var(--ink);
    letter-spacing: -0.5px;
  }
  .brand-rule {
    position: absolute; left: 266px; top: 152px;
    width: 592px; height: 3px; background: var(--brand-red);
  }
  .brand-tagline {
    position: absolute; left: 266px; top: 166px;
    font-family: "Oswald", sans-serif; font-weight: 500;
    font-size: 25px; line-height: 1; letter-spacing: 9.6px;
    color: var(--ink); text-transform: uppercase;
  }
  .accent-band {
    position: absolute; left: 0; top: 250px; width: 100%; height: 16px;
    background: linear-gradient(180deg, var(--brand-red) 0%, var(--brand-red-deep) 100%);
  }
  .contact-panel {
    position: absolute; left: 0; top: 266px; width: 100%; height: 274px;
    background: linear-gradient(160deg, var(--panel-charcoal) 0%, var(--panel-black) 70%);
    color: var(--text-light);
    font-family: "Old Standard TT", serif;
  }
  .person-name {
    position: absolute; left: 50px; top: 22px;
    font-weight: 700; font-size: 36px; color: var(--brand-red); line-height: 1;
  }
  .person-role {
    position: absolute; left: 50px; top: 66px;
    font-size: 22px; line-height: 1;
  }
  .contact-list {
    position: absolute; left: 50px; top: 110px; list-style: none;
  }
  .contact-item {
    display: flex; align-items: flex-start; gap: 10px;
    font-size: 27px; line-height: 31px;
  }
  .contact-icon { width: 26px; height: 28px; flex: none; margin-top: 2px; }
  .company-number {
    position: absolute; left: 86px; top: 244px;
    font-size: 18px; line-height: 1;
  }
</style>
</head>
<body>
<main class="canvas">
  <article class="business-card">
    <header class="brand-area">
      <div class="brand-mark" aria-hidden="true"></div>
      <h1 class="brand-name">Harwick Group</h1>
      <div class="brand-rule"></div>
      <p class="brand-tagline">Investment Management</p>
    </header>
    <div class="accent-band"></div>
    <section class="contact-panel">
      <h2 class="person-name">Maureen Blake</h2>
      <p class="person-role">Director</p>
      <ul class="contact-list">
        <li class="contact-item">
          <svg class="contact-icon" viewBox="0 0 26 28" aria-hidden="true">
            <rect x="6" y="1" width="14" height="26" rx="3" fill="var(--brand-red)"/>
            <rect x="9" y="5" width="8" height="8" fill="var(--panel-black)"/>
            <rect x="9" y="17" width="8" height="6" fill="var(--panel-black)" opacity="0.5"/>
          </svg>
          <span>+61 438 907 615</span>
        </li>
        <li class="contact-item">
          <svg class="contact-icon" viewBox="0 0 26 28" aria-hidden="true">
            <rect x="1" y="7" width="24" height="17" rx="2" fill="var(--brand-red)"/>
            <path d="M2 8 L13 17 L24 8" fill="none" stroke="var(--panel-black)" stroke-width="2"/>
          </svg>
          <span>maureen@harwickgroup.com.au</span>
        </li>
        <li class="contact-item">
          <svg class="contact-icon" viewBox="0 0 26 28" aria-hidden="true">
            <path d="M13 3 L25 14 H21 V26 H15 V19 H11 V26 H5 V14 H1 Z" fill="var(--brand-red)"/>
          </svg>
          <span>Level 1, 317 Carrow<br>St Townsville, Qld 4810</span>
        </li>
      </ul>
      <p class="company-number">ABN 48 317 602 559</p>
    </section>
  </article>
</main>
</body>
</html>
```